Kindro - Bringing Warmth and Quality to Senior Living

We are a new company based in Sydney, Australia. We have developed a state-of-the-art app for communication between aged care facilities and families.

Kindro has been developed for facilities to augment the best possible care by providing easy, safe and secure communication for families to stay in touch with their loved ones.
Updates

the website needs to be designed so we can add functionality including multilingual support. display in different languages.we also require enquiry and email/data base function. we want it simple and clean so its responsive. the target audience will be 40+ in age. there will be a video on home page. would like to start with 6 pages/ subjects -homepage -about us -our solution -demonstration page, this will be a page that contains videos of people using our product -customer testimonials -contact us

Target Market(s)

Aged care facilities.
Families (over 40’s age group) who are looking for a facility for their loved ones.

Number of Pages Required

5+ page

Font styles to use
Sans Serif

Colors
faa54b
ffffff
0255a3

Requirements
Must have
• - Our corporate colour is #EE8811.
• - If you're using stock photography, please use brimlo prints photos as we have a license for their photos.
• - The design needs to be responsive (mobile and desktop)
• -White space on each page
Nice to have
• -need to leave a place for a future animation video to be added in on the home tab
Should not have
• we don't want flash technology

```html
<!DOCTYPE html>
<html lang="en">
<head>
<meta charset="utf-8">
<title>Kindro - Bringing Warmth and Quality to Senior Living</title>
<link href="https://fonts.googleapis.com/css2?family=Ubuntu:ital,wght@0,300;0,400;0,500;0,700;1,300;1,400;1,500&display=swap" rel="stylesheet">
<style>
:root{
  --orange:#ee8811;
  --orange-soft:#faa54b;
  --blue:#0255a3;
  --ink:#1e2530;
  --ink-deep:#161b23;
  --text:#3a3f47;
  --muted:#7a808a;
  --rail:#f1f2f4;
  --white:#ffffff;
}
*{box-sizing:border-box;margin:0;padding:0}
html,body{width:1200px;height:4276px;overflow:hidden}
body{position:relative;font-family:"Ubuntu",sans-serif;color:var(--text);background:var(--white)}
.abs{position:absolute}
.rail{left:0;top:638px;width:240px;height:3552px;background:var(--rail)}
.sidebar{left:0;top:0;width:240px;height:638px;background:var(--ink);color:var(--white)}
.brand{position:absolute;left:40px;top:40px;display:flex;align-items:center;gap:10px}
.brand-dot{width:38px;height:38px;border-radius:50%;background:var(--orange)}
.nav{position:absolute;left:46px;top:148px;list-style:none}
.nav li{font-size:15px;height:43px;line-height:24px}
.nav li.active{font-weight:500;font-size:17px}
.nav li.active span{border-bottom:3px solid var(--orange);padding-bottom:4px}
.legal{position:absolute;left:46px;top:506px;font-size:11px;line-height:15px;color:#b9bec7;width:150px}
.abn{position:absolute;left:46px;top:592px;font-size:10px;color:#b9bec7}
.hero{left:240px;top:0;width:960px;height:638px;background:linear-gradient(120deg,#8a80c9 0%,#6a5fb8 45%,#4a3fa0 100%)}
.hero-title{position:absolute;right:66px;top:186px;text-align:right;color:var(--white);font-weight:300;font-size:48px;line-height:60px}
.btn-solid{position:absolute;background:var(--orange);color:var(--white);font-size:14px;font-weight:500;display:flex;align-items:center;justify-content:center}
.btn-line{position:absolute;border:2px solid var(--blue);color:var(--blue);font-size:13px;font-weight:500;display:flex;align-items:center;justify-content:center}
.intro-text{left:305px;top:795px;width:370px;font-size:17px;line-height:29px}
.intro-text em{font-weight:500}
.photo{background:linear-gradient(135deg,#6b7480,#3c4552);box-shadow:0 16px 30px rgba(0,0,0,.18)}
h2.section{color:var(--blue);font-weight:500;font-size:34px}
.sub{font-size:13px;line-height:18px;color:var(--muted)}
.feature{width:250px;font-size:17px;line-height:29px}
.feature svg{display:block;margin-bottom:20px}
.benefits{left:240px;top:1710px;width:960px;height:479px;background:linear-gradient(90deg,#4c4f52,#3a3c3f 60%,#2e3034);color:var(--white);text-align:center}
.arrow-circle{position:absolute;width:38px;height:38px;border-radius:50%;background:rgba(255,255,255,.25);display:flex;align-items:center;justify-content:center}
.dots{position:absolute;display:flex;gap:6px}
.dot{width:9px;height:9px;border-radius:50%;border:1px solid rgba(255,255,255,.7)}
.dot.on{background:var(--white)}
.quote{left:420px;top:2365px;width:600px;text-align:center;font-style:italic;font-weight:300;font-size:18px;line-height:33px;color:#333}
.avatar{left:686px;top:2535px;width:60px;height:60px;border-radius:50%;background:linear-gradient(135deg,#c9b39a,#8d7866)}
.contact-band{left:305px;top:3796px;width:895px;height:394px;background:var(--ink)}
.field{position:absolute;background:var(--white);border-radius:24px;font-size:14px;color:#555;padding:0 20px;display:flex;align-items:center}
.social{width:34px;height:34px;border-radius:50%;border:1px solid #6c7380}
.footer{left:240px;top:4190px;width:960px;height:86px;background:var(--ink-deep);color:#9aa0aa;font-size:10px;letter-spacing:.5px}
</style>
</head>
<body>

<div class="abs rail"></div>

<aside class="abs sidebar">
  <div class="brand"><span class="brand-dot"></span><span style="font-size:18px;font-weight:500">Kindro</span></div>
  <ul class="nav">
    <li class="active"><span>Kindro</span></li>
    <li>About Us</li>
    <li>Solution</li>
    <li>Demonstration</li>
    <li>Testimonials</li>
    <li>Contact</li>
  </ul>
  <p class="legal">© 2019<br>Brightway Pty Ltd. All rights reserved.</p>
  <p class="abn">ABN 51 802 336 419</p>
</aside>

<section class="abs hero" role="img" aria-label="Carer smiling with an elderly woman, purple tinted photo">
  <h1 class="hero-title">Are you looking<br>for a facility for your<br>loved ones.</h1>
  <div class="btn-solid" style="left:737px;top:393px;width:157px;height:43px">Contact Us</div>
</section>

<p class="abs intro-text">Kindro has been <em>developed for facilities</em> to augment the best possible care by providing easy, safe and secure communication for families to stay in touch with their loved ones.</p>
<div class="btn-line" style="left:305px;top:980px;width:157px;height:40px">What is Kindro?</div>
<div class="abs photo" role="img" aria-label="Elderly residents enjoying music together" style="left:735px;top:752px;width:399px;height:320px"></div>

<h2 class="abs section" style="left:305px;top:1176px">Solutions We Provide</h2>
<p class="abs sub" style="left:305px;top:1226px;width:620px">Kindro complies with the requirements of Privacy Act 1988 (Cth). Information is protected as required by current Australian law.</p>

<div class="abs feature" style="left:305px;top:1311px">
  <svg width="52" height="68" viewBox="0 0 52 68" fill="none" stroke="#ee8811" stroke-width="2.5"><rect x="3" y="3" width="46" height="62" rx="6"/><line x1="18" y1="58" x2="34" y2="58"/><line x1="18" y1="40" x2="18" y2="30"/><line x1="26" y1="40" x2="26" y2="22"/><line x1="34" y1="40" x2="34" y2="27"/></svg>
  Provides frequent resident updates to families on mobile that easy to use.
</div>
<div class="abs feature" style="left:590px;top:1311px">
  <svg width="60" height="68" viewBox="0 0 60 68" fill="none" stroke="#ee8811" stroke-width="2.5"><path d="M3 3h36l10 10v50H3z"/><line x1="11" y1="18" x2="30" y2="18"/><line x1="11" y1="28" x2="30" y2="28"/><circle cx="44" cy="46" r="6"/><path d="M34 64c0-8 20-8 20 0"/></svg>
  Meal reports, Activities with associated photos and videos
</div>
<div class="abs feature" style="left:875px;top:1311px">
  <svg width="68" height="68" viewBox="0 0 68 68" fill="none" stroke="#ee8811" stroke-width="2.5"><path d="M3 16V3h13M52 3h13v13M65 52v13H52M16 65H3V52"/><path d="M10 34c10-14 38-14 48 0c-10 14-38 14-48 0z"/><circle cx="34" cy="34" r="7"/></svg>
  Residents privacy is ensured by the use of advanced artificial intelligence processes.
</div>
<div class="btn-line" style="left:305px;top:1550px;width:157px;height:40px">WHY Kindro?</div>

<section class="abs benefits" role="img" aria-label="Elderly woman receiving a cup of tea, darkened photo">
  <p style="position:absolute;left:0;right:0;top:1828px;top:118px;font-size:16px;font-weight:500">Kindro Benefits</p>
  <p style="position:absolute;left:0;right:0;top:196px;font-size:32px;font-weight:500;line-height:44px">Competitive advantage as Families<br>proof of excellent care.</p>
  <div class="arrow-circle" style="left:46px;top:221px"><svg width="12" height="14"><path d="M9 2L3 7l6 5" fill="none" stroke="#fff" stroke-width="2"/></svg></div>
  <div class="arrow-circle" style="left:876px;top:221px"><svg width="12" height="14"><path d="M3 2l6 5-6 5" fill="none" stroke="#fff" stroke-width="2"/></svg></div>
  <div class="dots" style="left:438px;top:372px"><span class="dot on"></span><span class="dot"></span><span class="dot"></span><span class="dot"></span><span class="dot"></span><span class="dot"></span></div>
</section>

<svg class="abs" style="left:698px;top:2300px" width="48" height="36" viewBox="0 0 48 36" fill="none" stroke="#ee8811" stroke-width="4"><path d="M18 4C8 8 4 16 4 30h14V18H8M42 4C32 8 28 16 28 30h14V18H32"/></svg>
<p class="abs quote">Lorem ipsum dolor sit amet, consectetur adipiscing elit, sed do eiusmod tempor incididunt ut labore et dolore magna aliqua. Ut enim ad minim veniam, nostrud exercitation ullamco laboris nisi ut aliquip ex ea ...</p>
<div class="abs" style="left:1068px;top:2405px;display:flex;flex-direction:column;gap:6px">
  <span style="width:10px;height:10px;border-radius:50%;background:#8aa6c8"></span>
  <span style="width:10px;height:10px;border-radius:50%;border:1px solid #8aa6c8"></span>
  <span style="width:10px;height:10px;border-radius:50%;border:1px solid #8aa6c8"></span>
  <span style="width:10px;height:10px;border-radius:50%;border:1px solid #8aa6c8"></span>
</div>
<div class="abs avatar" role="img" aria-label="Portrait of testimonial author"></div>
<p class="abs" style="left:570px;top:2610px;width:292px;text-align:center;font-size:13px;font-weight:700;color:#222">Daniel Whitmore</p>

<div class="abs photo" role="img" aria-label="Couple watching a video on a phone" style="left:305px;top:2747px;width:829px;height:479px;background:linear-gradient(135deg,#c9ccd0,#9ea4ab 55%,#7d848c)">
  <svg style="position:absolute;left:394px;top:219px" width="42" height="42" viewBox="0 0 42 42"><circle cx="21" cy="21" r="19" fill="none" stroke="#fff" stroke-width="2.5"/><path d="M17 13l11 8-11 8z" fill="#fff"/></svg>
</div>

<h2 class="abs section" style="left:305px;top:3336px;width:380px;font-size:33px;line-height:44px">We are a Sydney based family owned company based in Sydney, Australia.</h2>
<p class="abs" style="left:735px;top:3340px;width:400px;font-size:17px;line-height:28px">We have developed a state-of-the-art app for communication between aged care facilities and families.</p>
<p class="abs sub" style="left:735px;top:3452px;width:400px;font-size:14px;line-height:22px">Our backgrounds encompass 40 years of software development, decades of experience in marketing, management and service delivery and over 10 years within the childcare industry.</p>
<div class="btn-line" style="left:735px;top:3580px;width:162px;height:40px">Who Are We?</div>

<div class="abs contact-band"></div>
<div class="abs" role="img" aria-label="Team member portrait" style="left:240px;top:3705px;width:139px;height:180px;background:linear-gradient(135deg,#d8d8d8,#9a9a9a)"></div>
<div class="abs" role="img" aria-label="Team member portrait" style="left:413px;top:3705px;width:183px;height:180px;background:linear-gradient(135deg,#e2e2e2,#a8a8a8)"></div>
<div class="abs" role="img" aria-label="Team member portrait" style="left:627px;top:3705px;width:182px;height:180px;background:linear-gradient(135deg,#dcdcdc,#a0a0a0)"></div>
<div class="arrow-circle" style="left:393px;top:3775px;width:34px;height:34px;background:var(--blue)"><svg width="10" height="12"><path d="M7 1L2 6l5 5" fill="none" stroke="#fff" stroke-width="2"/></svg></div>
<div class="arrow-circle" style="left:578px;top:3775px;width:34px;height:34px;background:var(--blue)"><svg width="10" height="12"><path d="M3 1l5 5-5 5" fill="none" stroke="#fff" stroke-width="2"/></svg></div>
<div class="abs" style="left:812px;top:3705px;width:388px;height:91px;background:var(--white)"></div>
<h2 class="abs" style="left:889px;top:3752px;font-size:44px;font-weight:700;color:#111">Contact Us</h2>

<p class="abs" style="left:305px;top:3908px;width:395px;text-align:center;color:var(--white);font-size:28px;font-weight:500">Maya Thornton</p>
<p class="abs" style="left:305px;top:3952px;width:395px;text-align:center;color:#c3c8d0;font-size:13px">Marketing Consultant</p>
<div class="abs" style="left:305px;top:3990px;width:395px;height:1px;background:#3d4552"></div>
<p class="abs" style="left:305px;top:4036px;width:395px;text-align:center;color:#aab0ba;font-size:20px;font-weight:300">P. 9000 4417 &nbsp;/ E. hello@kindro.au</p>
<div class="abs" style="left:414px;top:4107px;display:flex;gap:18px"><span class="social"></span><span class="social"></span><span class="social"></span><span class="social"></span></div>

<div class="field" style="left:735px;top:3865px;width:191px;height:46px">Your Name</div>
<div class="field" style="left:949px;top:3865px;width:185px;height:46px">Email</div>
<div class="field" style="left:735px;top:3927px;width:191px;height:46px">Phone</div>
<div class="field" style="left:949px;top:3927px;width:185px;height:46px">Subject</div>
<div class="field" style="left:735px;top:3990px;width:399px;height:134px;align-items:flex-start;padding-top:14px;border-radius:20px">Message ...</div>
<div class="abs" style="left:1064px;top:4100px;width:48px;height:48px;border-radius:50%;background:var(--orange);display:flex;align-items:center;justify-content:center"><svg width="22" height="20" viewBox="0 0 22 20"><path d="M1 1l20 9-20 9 3-9z" fill="#fff"/></svg></div>

<footer class="abs footer">
  <p style="position:absolute;left:160px;top:38px">PRIVACY POLICY &nbsp;|&nbsp; TERMS OF USE &nbsp;|&nbsp; LEGAL</p>
  <svg style="position:absolute;left:920px;top:30px" width="14" height="22" viewBox="0 0 14 22"><path d="M7 21V2M1 8l6-6 6 6" fill="none" stroke="#9aa0aa" stroke-width="2"/></svg>
</footer>

</body>
</html>
```